redesign of my existing custom website into Wordpress based website

I need someone to redesign my current website into something more classy, simplistic, modern and on trend. I would like it set up on Wordpress in a way thats easy for me to make my own additions to blogs/price changes and promotion banners. I will also need a page that is password protected so members can login and have access to all my training videos and resources.
website is www.lilacnestfit.com.au

Target Market(s)

new mums

Industry/Entity Type

Fitness

Colors
33a6d7

Requirements
Must have
• chic, modern, stylish and simplistic.
• a call to action above the page fold
• mobile friendly conversion
• a pop up message as soon as someone enters my sight offering my free report
• a members page that is password protected containing 3 youtube videos and 6 pdf attachments as resources
• a home page
• a contact us page
• an about us page
• a blog page
• a store page
Nice to have
• some examples of my peers websites that I like:
• www.norahvale.com
• https://www.7qpz.com
• https://41withdaxford.com
Should not have
• anything gimmicky

```html
<!DOCTYPE html>
<html lang="en">
<head>
<meta charset="utf-8">
<title>Lilac Nest Fit — Home</title>
<link href="https://fonts.googleapis.com/css2?family=Jost:wght@300;400;500&family=Open+Sans:wght@400;600&display=swap" rel="stylesheet">
<style>
:root{
  --brand:#33a6d7;
  --brand-deep:#2b8fbc;
  --footer:#2e86b0;
  --footer-strip:#256e91;
  --ink:#3a3a3a;
  --muted:#777;
  --line:#e4e4e4;
  --white:#fff;
  --dim:rgba(0,0,0,.55);
}
*{box-sizing:border-box;margin:0;padding:0}
html,body{width:1200px;height:3529px;overflow:hidden}
body{position:relative;font-family:"Open Sans",Arial,sans-serif;color:var(--ink);background:var(--white)}
h1,h2,h3,h4,.nav,.btn{font-family:"Jost",Arial,sans-serif}

/* header */
.site-header{position:absolute;top:0;left:0;width:1200px;height:106px;background:var(--white);z-index:2}
.logo{position:absolute;left:134px;top:-8px;width:180px;height:180px;border-radius:50%;background:var(--white);border:4px solid #8a8a8a;display:flex;align-items:center;justify-content:center;text-align:center;font-family:"Jost",sans-serif;font-weight:400;font-size:22px;color:#9b2a5a;line-height:1.1}
.top-links{position:absolute;right:106px;top:20px;font-size:11px;color:var(--muted);font-family:"Jost",sans-serif;letter-spacing:.5px}
.top-links span{margin:0 8px}
.nav{position:absolute;left:600px;top:68px;display:flex;gap:38px;font-size:12px;letter-spacing:.6px;color:var(--ink)}
.nav a{color:inherit;text-decoration:none;padding-bottom:8px}
.nav a.active{color:var(--brand);border-bottom:2px solid var(--brand)}

/* hero */
.hero{position:absolute;top:106px;left:0;width:1200px;height:494px;background:linear-gradient(100deg,#b9b3ab 0%,#d6d0c8 35%,#c7c1b8 70%,#a9a39b 100%)}
.hero h1{position:absolute;top:148px;left:0;width:1200px;text-align:center;color:var(--white);font-weight:300;font-size:40px;line-height:56px;letter-spacing:.5px}
.signup-band{position:absolute;top:600px;left:0;width:1200px;height:101px;background:var(--brand)}
.signup-band p{position:absolute;left:134px;top:24px;color:var(--white);font-family:"Jost",sans-serif;font-size:20px;line-height:26px;width:330px}
.signup-band .field{position:absolute;left:740px;top:28px;width:195px;height:40px;background:var(--white)}
.signup-band .go{position:absolute;left:945px;top:28px;width:123px;height:40px;background:#3b3b3b;color:var(--white);font-size:12px;display:flex;align-items:center;justify-content:center;font-family:"Jost",sans-serif}

/* welcome */
.welcome h2{position:absolute;left:134px;top:760px;font-weight:400;font-size:30px;color:var(--brand-deep);letter-spacing:.3px}
.welcome p{position:absolute;left:134px;top:816px;width:490px;font-size:11.5px;line-height:23px;color:var(--muted)}
.btn{display:flex;align-items:center;justify-content:center;background:var(--brand);color:var(--white);font-size:13px;border-radius:2px}
.welcome .btn{position:absolute;left:134px;top:984px;width:99px;height:38px}
.video{position:absolute;left:645px;top:777px;width:414px;height:237px;background:linear-gradient(135deg,#6d625c,#a69a94 50%,#7b6f78)}
.video svg{position:absolute;left:177px;top:88px}

/* program */
.program{position:absolute;top:1118px;left:0;width:1200px;height:489px;background:radial-gradient(circle at 50% 50%,#3fb0df,var(--brand) 60%,#2f9bc9)}
.program .photo{position:absolute;left:200px;top:0;width:360px;height:489px;background:linear-gradient(135deg,#5fb9de 0%,#8cc7c2 55%,#7fbfa8 100%)}
.program h2{position:absolute;left:544px;top:82px;font-weight:300;font-size:28px;color:var(--white);letter-spacing:.5px}
.feature{position:absolute;left:544px;display:flex;align-items:center;gap:26px;color:var(--white);font-family:"Jost",sans-serif;font-weight:300;font-size:20px;line-height:25px}
.feature svg{flex:none}

/* results */
.results h2{position:absolute;top:1670px;left:0;width:1200px;text-align:center;font-weight:400;font-size:29px;color:var(--brand-deep)}
.avatar{position:absolute;top:1746px;width:70px;height:70px;border-radius:50%;border:3px solid #ddd}
.results p{position:absolute;left:134px;top:1836px;width:932px;text-align:center;font-size:11px;line-height:23px;color:var(--muted)}
.results .name{position:absolute;top:1934px;left:0;width:1200px;text-align:center;color:var(--brand);font-family:"Jost",sans-serif;font-size:18px}
.results .role{position:absolute;top:1970px;left:0;width:1200px;text-align:center;font-size:11px;color:var(--muted)}
.dots{position:absolute;top:2003px;left:586px;display:flex;gap:6px}
.dots i{width:7px;height:7px;border-radius:50%;background:#ccc}
.dots i.on{background:var(--brand)}

/* workout */
.workout{position:absolute;top:2078px;left:0;width:1200px;height:444px;background:linear-gradient(120deg,#3a3836,#57534e 45%,#3f3b38)}
.workout h2{position:absolute;top:96px;left:0;width:1200px;text-align:center;font-weight:300;font-size:33px;color:var(--white);letter-spacing:.5px}
.workout ul{position:absolute;top:160px;left:0;width:1200px;list-style:none;text-align:center;color:#eee;font-size:12.5px;line-height:23px}
.workout .btn{position:absolute;left:535px;top:294px;width:130px;height:42px}

/* news */
.news h2{position:absolute;top:2578px;left:0;width:1200px;text-align:center;font-weight:400;font-size:29px;color:var(--brand-deep)}
.card{position:absolute;top:2673px;width:290px;height:445px;border:1px solid var(--line);background:var(--white)}
.card .thumb{height:202px}
.card h3{position:absolute;left:18px;top:236px;font-weight:400;font-size:18px;line-height:26px;color:var(--ink)}
.card p{position:absolute;left:18px;top:300px;width:250px;font-size:10.5px;line-height:19px;color:var(--muted)}
.card .btn{position:absolute;left:18px;top:362px;width:108px;height:40px}

/* footer */
.site-footer{position:absolute;top:3165px;left:0;width:1200px;height:364px;background:var(--footer);color:#e6f3fa}
.site-footer h4{position:absolute;top:42px;font-weight:400;font-size:14px;letter-spacing:.5px;color:var(--white)}
.site-footer ul{position:absolute;top:88px;list-style:none;font-size:11px;line-height:22px}
.contact-list li{display:flex;gap:10px;align-items:flex-start}
.contact-list li::before{content:"";width:11px;height:11px;background:#e6f3fa;margin-top:5px;flex:none}
.site-footer .note{position:absolute;left:565px;top:88px;width:250px;font-size:11px;line-height:20px}
.site-footer .field{position:absolute;left:565px;top:160px;width:250px;height:40px;background:var(--white);color:#999;font-size:11px;padding:12px}
.site-footer .go{position:absolute;left:565px;top:214px;width:82px;height:30px;background:#333;color:var(--white);font-size:11px;display:flex;align-items:center;justify-content:center}
.social{position:absolute;left:892px;top:102px;display:flex;gap:8px}
.social i{width:30px;height:30px;border-radius:50%;border:1.5px solid #e6f3fa}
.copyright{position:absolute;bottom:0;left:0;width:1200px;height:58px;background:var(--footer-strip);text-align:center;font-size:10.5px;line-height:58px;color:#dcebf3}

/* overlay + popup */
.dimmer{position:absolute;inset:0;background:var(--dim);z-index:5}
.popup{position:absolute;left:292px;top:365px;width:619px;height:336px;background:var(--white);z-index:6}
.popup .photo{position:absolute;left:40px;top:10px;width:195px;height:326px;background:linear-gradient(160deg,#eeeeee 0%,#dfe6dc 60%,#cfdcc8 100%)}
.popup h2{position:absolute;left:360px;top:56px;width:220px;text-align:right;font-family:"Jost",sans-serif;font-weight:400;font-size:28px;color:#111}
.popup .lead{position:absolute;left:252px;top:108px;width:328px;text-align:right;font-size:11px;color:#222}
.popup .field{position:absolute;left:250px;top:149px;width:327px;height:47px;border:1px solid #cfcfcf;font-size:11px;color:#333;padding:16px 14px}
.popup .btn{position:absolute;left:421px;top:212px;width:158px;height:47px;font-size:13px;background:#2d93d2}
</style>
</head>
<body>

<header class="site-header">
  <div class="logo">Lilac<br>Nest Fit</div>
  <div class="top-links">SIGN UP<span>|</span>REGISTER<span>|</span>&#9679; MY CART</div>
  <nav class="nav">
    <a class="active">HOME</a><a>ABOUT US</a><a>PROGRAM</a><a>BLOG</a><a>SHOP</a><a>CONTACT US</a>
  </nav>
</header>

<section class="hero" role="img" aria-label="Photo of a smiling mum in workout gear inside a bright living room">
  <h1>LOSE YOUR BABY WEIGHT AND BOUNCE<br>BACK INTO SHAPE!</h1>
</section>

<section class="signup-band">
  <p>GET YOUR FREE TOP 10 FAT<br>BLASTING TIPS</p>
  <div class="field"></div>
  <div class="go">SUBSCRIBE</div>
</section>

<section class="welcome">
  <h2>WELCOME TO LILACNESTFIT</h2>
  <p>Hello and welcome! I am a mum of two, a qualified personal trainer and a passionate believer that every new mum deserves to feel strong again. After two pregnancies I know how hard it is to find time for yourself, so I created a simple home program that fits around naps, school runs and busy days. My approach is gentle, safe and realistic, built to help you regain your energy, confidence and fitness one week at a time. Join our friendly community and start your journey today.</p>
  <div class="btn">Read More</div>
  <div class="video" role="img" aria-label="Video still of a mum exercising on the floor beside her baby">
    <svg width="60" height="60" viewBox="0 0 60 60"><circle cx="30" cy="30" r="29" fill="rgba(255,255,255,.85)"/><path d="M24 18 L44 30 L24 42 Z" fill="#555"/></svg>
  </div>
</section>

<section class="program">
  <div class="photo" role="img" aria-label="Photo of the trainer in a sports vest"></div>
  <h2>WHAT'S INCLUDED IN THE PROGRAM?</h2>
  <div class="feature" style="top:165px">
    <svg width="44" height="40" viewBox="0 0 44 40" fill="none" stroke="#fff" stroke-width="2"><path d="M22 37 C8 27 2 20 2 12 A9 9 0 0 1 22 8 A9 9 0 0 1 42 12 C42 20 36 27 22 37 Z"/><path d="M6 20 H15 L18 13 L23 27 L27 18 H38"/></svg>
    <span>OUR UNIQUE 3 STAGE, 12 WEEK<br>TRAINING PROGRAM</span>
  </div>
  <div class="feature" style="top:252px">
    <svg width="44" height="40" viewBox="0 0 44 40" fill="#fff"><rect x="2" y="14" width="6" height="12"/><rect x="36" y="14" width="6" height="12"/><rect x="9" y="10" width="5" height="20"/><rect x="30" y="10" width="5" height="20"/><rect x="14" y="18" width="16" height="4"/></svg>
    <span>FULL INSTRUCTIONAL WORKOUT DVD AND<br>PROGRAM CARDS FOR EACH PROGRAM</span>
  </div>
  <div class="feature" style="top:364px">
    <svg width="44" height="40" viewBox="0 0 44 40" fill="none" stroke="#fff" stroke-width="2"><path d="M2 38 H42"/><rect x="6" y="26" width="6" height="12"/><rect x="16" y="18" width="6" height="20"/><rect x="26" y="10" width="6" height="28"/><rect x="36" y="2" width="6" height="36"/></svg>
    <span>WEEKLY ACCOUNTABILITY CHARTS</span>
  </div>
</section>

<section class="results">
  <h2>CHECK OUT SOME OF THE AWESOME RESULTS ALREADY ACHIEVED</h2>
  <div class="avatar" role="img" aria-label="Member portrait" style="left:526px;background:linear-gradient(135deg,#8fc6e0,#3f7fa8)"></div>
  <div class="avatar" role="img" aria-label="Member portrait" style="left:604px;background:linear-gradient(135deg,#c9a48a,#7a5a48)"></div>
  <p>After the birth of my second baby I felt tired, heavy and unsure where to begin. This program changed everything for me. The workouts were short enough to fit into nap time and the meal guides made healthy eating easy for the whole family. Within twelve weeks I had lost eight kilos, my back pain was gone and I finally felt like myself again. The support from the other mums kept me going on the hard days and I now look forward to every session. Thank you for giving me my confidence back.</p>
  <div class="name">Marisol</div>
  <div class="role">Mum of two, Member</div>
  <div class="dots"><i></i><i class="on"></i><i></i></div>
</section>

<section class="workout" role="img" aria-label="Photo of a mum working out on a mat in a dim living room">
  <h2>12 WEEK HOME WORKOUT PROGRAM</h2>
  <ul>
    <li>Our 3 stage, 12 week training program</li>
    <li>Full Instructional Workout DVD for each program</li>
    <li>Nutritionist approved healthy eating guidelines</li>
    <li>Healthy Family recipes you can all enjoy</li>
  </ul>
  <div class="btn">Read More</div>
</section>

<section class="news">
  <h2>RECENT NEWS</h2>
  <article class="card" style="left:134px">
    <div class="thumb" role="img" aria-label="Home gym corner with a framed print" style="background:linear-gradient(135deg,#3b3532,#6e625b)"></div>
    <h3>THE BENEFITS OF TRAINING<br>IN THE MORNING</h3>
    <p>An early session lifts your mood, boosts energy and sets a healthy tone for the whole day.</p>
    <div class="btn">Read More</div>
  </article>
  <article class="card" style="left:456px">
    <div class="thumb" role="img" aria-label="Baby crawling on a living room floor" style="background:linear-gradient(135deg,#4a4542,#8a7e78)"></div>
    <h3>THE BENEFITS OF TRAINING<br>IN THE MORNING</h3>
    <p>An early session lifts your mood, boosts energy and sets a healthy tone for the whole day.</p>
    <div class="btn">Read More</div>
  </article>
  <article class="card" style="left:779px">
    <div class="thumb" role="img" aria-label="Trainer stretching on a yoga mat" style="background:linear-gradient(135deg,#7a6a6a,#6a5a8a)"></div>
    <h3>THE BENEFITS OF TRAINING<br>IN THE MORNING</h3>
    <p>An early session lifts your mood, boosts energy and sets a healthy tone for the whole day.</p>
    <div class="btn">Read More</div>
  </article>
</section>

<footer class="site-footer">
  <h4 style="left:134px">CONTACT US</h4>
  <ul class="contact-list" style="left:134px;width:210px">
    <li>0400 123 456</li>
    <li>07 5555 0199</li>
    <li>hello@lilacnestfit.com.au</li>
    <li>PO Box 42, Harbourview QLD 4000, Australia</li>
  </ul>
  <h4 style="left:370px">QUICK LINKS</h4>
  <ul style="left:370px">
    <li>Home</li><li>About Us</li><li>Program</li><li>Blog</li><li>Shop</li><li>Contact Us</li>
  </ul>
  <h4 style="left:565px">NEWSLETTER</h4>
  <p class="note">Sign up for our newsletter to receive fitness tips, recipes and special offers straight to your inbox.</p>
  <div class="field">Enter Your Mail Id</div>
  <div class="go">Subscribe</div>
  <h4 style="left:892px">FOLLOW US</h4>
  <div class="social"><i></i><i></i><i></i><i></i><i></i></div>
  <div class="copyright">Copyright © 2015 Lilac Nest Fit. All rights reserved.</div>
</footer>

<div class="dimmer"></div>

<div class="popup">
  <div class="photo" role="img" aria-label="Photo of the trainer in a sports vest"></div>
  <h2>MY FREE REPORT</h2>
  <p class="lead">Lorem ipsum dolor sit amet, consectetur adipiscing elit,</p>
  <div class="field">Enter Your Mail Id</div>
  <div class="btn">SUBSCRIBE</div>
</div>

</body>
</html>
```